Window Tinting Website Design

We are working with a Window Tinting company in California. They do commercial, residential, and automotive tint.

Some websites for inspiration:
https://www.velmoshadez.com/
https://www.qpridegleam.com/
https://drobfinishx.com/

Thank you for taking the time to consider designing a website for us. We are web developers based in Stockton, CA, USA. Most of our projects go through the same process. Understanding this process may help you win a project with us. We custom-code all of our websites in-house. We don’t have any requirements as to what tools you use for your design, but we ask that you follow these guidelines.

IMAGES:
If you use any images or icons in the design, we ask that you have a link to the asset so we can purchase the image/icon. Most of the designs we submit do not have the customer’s images on them unless they have some great images. Be creative; show us the feeling you are trying to portray with your image choices. Use any royalty-free site you choose. We subscribe to Brenlo and mainly use their images, but we can purchase images outside of Brenlo. PLEASE NOTE: we will not submit designs to clients with watermarks on the images.

FONTS:
We ask that you identify the fonts you’re using in the design. This can be done in a message if you want. We typically use Google Fonts and Brenlo Fonts.

CONTENT:
We're always open to different content and ideas. We often submit designs with stock images so the client can see our vision. We typically take pictures after the website launch to use their images with our vision. Lorem Ipsum is fine for paragraphs, but we ask that you make the Headers with correct English. We want to be able to show the vision and identify the sections of the website.

INSPIRATION:
We typically add a couple of links in the brief of websites we like to help you get started in your design.

REVISIONS:
We do not often ask for revisions of the designs unless we see something in the design that may not appeal to the client. If there are slight changes that we want to make, we do that in the development process.

FEEDBACK:
We rarely give feedback on designs during the design process. We are working on many website projects and do not have the time to provide feedback. We usually respond if your request is well thought out and asks specific questions, but a note asking “feedback, please” usually goes unanswered.

```html
<!DOCTYPE html>
<html lang="en">
<head>
<meta charset="utf-8">
<title>Brightline Tint — Window Tinting</title>
<link rel="stylesheet" href="https://fonts.googleapis.com/css2?family=Oswald:wght@400;500;600&family=Poppins:wght@400;500;600&display=swap">
<style>
:root{
  --red:#d42030;
  --red-dark:#b3161f;
  --steel:#4d7594;
  --navy:#2d4a61;
  --ink:#222;
  --muted:#555;
  --card:#efefef;
  --black:#0c0c0c;
  --mist:#c3ccd4;
  --foot:#f2f2f2;
  --gold:#f2b705;
}
*{box-sizing:border-box;margin:0;padding:0}
html,body{width:1200px;height:4240px;overflow:hidden}
body{position:relative;background:#fff;font-family:'Poppins',sans-serif;color:var(--ink)}
.abs{position:absolute}
.display{font-family:'Oswald',sans-serif;text-transform:uppercase}
.btn{position:absolute;background:var(--red);color:#fff;font-family:'Oswald',sans-serif;font-weight:500;text-transform:uppercase;display:flex;align-items:center;justify-content:center;border-radius:0 14px 0 14px;font-size:14px}

/* header */
.site-header{position:absolute;left:0;top:0;width:1200px;height:80px;background:#fff;border-top:3px solid var(--red)}
.brand{position:absolute;left:140px;top:20px;display:flex;align-items:center;gap:10px;font-family:'Oswald',sans-serif;font-weight:600;font-size:20px;color:var(--red);text-transform:uppercase}
.brand-dot{width:14px;height:14px;border-radius:50%;background:var(--red)}
.nav{position:absolute;left:336px;top:30px;display:flex;gap:36px;font-family:'Oswald',sans-serif;font-style:italic;font-size:11px;text-transform:uppercase;color:#333}
.nav .active{color:var(--red)}
.header-phone{position:absolute;left:826px;top:28px;font-family:'Oswald',sans-serif;font-style:italic;font-size:15px;color:var(--red)}
.header-cta{left:938px;top:23px;width:120px;height:34px}

/* hero */
.hero{position:absolute;left:0;top:80px;width:1200px;height:612px;background:linear-gradient(100deg,#2a2c30 0%,#4b4f55 45%,#8a8f95 75%,#5a5e63 100%)}
.hero-accent{position:absolute;left:0;top:0;width:1200px;height:612px}
.hero-title{position:absolute;left:140px;top:165px;font-size:68px;line-height:80px;color:#fff;font-weight:500}
.hero-tags{position:absolute;left:140px;top:347px;display:flex;gap:18px;font-family:'Oswald',sans-serif;font-size:15px;letter-spacing:1px;color:#fff;text-transform:uppercase}
.hero-tags span{display:flex;align-items:center;gap:8px}
.hero-tags span::before{content:"";width:9px;height:9px;border-radius:50%;background:var(--red);box-shadow:0 0 0 3px rgba(212,32,48,.35)}
.hero-cta{left:140px;top:395px;width:120px;height:32px}
.hero-rule{position:absolute;left:140px;top:546px;width:928px;height:1px;background:rgba(255,255,255,.35)}
.hero-links{position:absolute;top:569px;font-family:'Oswald',sans-serif;font-style:italic;font-size:11px;color:#fff;text-transform:uppercase}

/* section titles */
.section-title{position:absolute;left:0;width:1200px;display:flex;align-items:center;justify-content:center;gap:24px;font-family:'Oswald',sans-serif;text-transform:uppercase;font-size:38px;font-weight:500}
.section-title::before,.section-title::after{content:"";height:1px;width:190px;background:currentColor;opacity:.6}
.lead{position:absolute;left:0;width:1200px;text-align:center;font-size:12.5px;line-height:21px}

/* services */
.services .section-title{top:760px;color:var(--steel)}
.services .lead{top:820px;color:#444}
.service-card{position:absolute;top:897px;width:262px;height:254px;background:var(--card);text-align:center}
.service-card::before{content:"";position:absolute;left:0;top:0;width:50px;height:26px;border-left:2px solid var(--red);border-top:2px solid var(--red);transform:translate(-2px,-2px)}
.service-card::after{content:"";position:absolute;right:0;bottom:0;width:26px;height:50px;border-right:2px solid var(--red);border-bottom:2px solid var(--red);transform:translate(2px,2px)}
.service-card svg{margin-top:18px}
.service-card h3{font-family:'Oswald',sans-serif;font-weight:500;font-size:18px;text-transform:uppercase;margin-top:10px;color:#222}
.service-card p{font-size:11px;line-height:19px;color:#555;margin:8px 16px 0}
.service-card .more{display:inline-block;margin-top:10px;font-family:'Oswald',sans-serif;font-size:12px;text-decoration:underline;color:#222;text-transform:uppercase}
.all-services{left:525px;top:1195px;width:150px;height:35px}

/* why us */
.why{position:absolute;left:0;top:1312px;width:1200px;height:574px;background:radial-gradient(ellipse at 50% 80%,#40647f 0%,var(--navy) 70%)}
.why .section-title{top:70px;color:#fff}
.why .lead{top:124px;color:#e8eef3}
.why-cta{left:525px;top:188px;width:150px;height:34px}
.stat{position:absolute}
.stat-num{position:absolute;left:0;width:100%;text-align:center;font-family:'Oswald',sans-serif;font-weight:500;line-height:1}
.stat-label{position:absolute;left:0;width:100%;text-align:center;font-family:'Oswald',sans-serif;font-size:15px;line-height:18px;text-transform:uppercase}

/* work */
.work{position:absolute;left:0;top:1886px;width:1200px;height:954px;background:radial-gradient(ellipse at 50% 40%,#1c1c1c 0%,var(--black) 75%)}
.work .section-title{top:70px;color:#fff}
.work-tile{position:absolute;width:415px;height:339px}
.work-tile span{position:absolute;left:36px;bottom:30px;font-family:'Oswald',sans-serif;font-weight:500;font-size:19px;letter-spacing:1px;color:#fff;text-transform:uppercase}

/* testimonials */
.testimonials .section-title{top:2910px;color:var(--steel)}
.quote-card{position:absolute;background:#fff;box-shadow:0 0 14px rgba(0,0,0,.12);text-align:center}
.avatar{position:absolute;left:50%;transform:translateX(-50%);border-radius:50%;border:3px solid #fff;box-shadow:0 0 6px rgba(0,0,0,.2)}
.quote-mark{font-family:'Oswald',sans-serif;font-size:44px;color:var(--red);line-height:1;font-weight:600}
.quote-card p{font-size:12px;line-height:22px;color:#444}
.quote-card h4{font-size:15px;color:var(--red);font-weight:500;margin-top:22px}
.stars{color:var(--gold);font-size:17px;letter-spacing:1px;line-height:1}

/* project */
.foot-band{position:absolute;left:0;top:3700px;width:1200px;height:540px;background:var(--foot)}
.project{position:absolute;left:112px;top:3465px;width:976px;height:380px;background:var(--mist);overflow:hidden}
.project h2{position:absolute;left:56px;top:72px;font-size:38px;font-weight:500;color:#111}
.project p{position:absolute;left:56px;top:148px;width:500px;font-size:13px;line-height:25px;color:#333}
.signup{position:absolute;left:56px;top:240px;width:388px;height:56px;background:#fff;display:flex;align-items:center;padding:0 10px 0 14px;justify-content:space-between;font-size:13px;color:#333}
.signup .btn{position:static;width:146px;height:36px;border-radius:0}

/* footer */
.footer-brand{position:absolute;left:168px;top:3912px;display:flex;align-items:center;gap:10px;font-family:'Oswald',sans-serif;font-weight:600;font-size:22px;color:var(--red);text-transform:uppercase}
.footer-about{position:absolute;left:168px;top:3976px;width:240px;font-size:12px;line-height:21px;color:#333}
.socials{position:absolute;left:170px;top:4079px;display:flex;gap:12px}
.socials span{width:21px;height:21px;border-radius:50%;background:var(--red)}
.foot-col{position:absolute;top:3908px}
.foot-col h5{font-family:'Oswald',sans-serif;font-weight:500;font-size:15px;color:#222;padding-bottom:6px;position:relative}
.foot-col h5::after{content:"";position:absolute;left:0;bottom:0;width:30px;height:2px;background:var(--red)}
.foot-col ul{list-style:none;margin-top:12px}
.foot-col li{font-size:11.5px;line-height:28px;color:#333}
.contact-row{display:flex;gap:10px;font-size:11.5px;color:#333;line-height:15px;margin-bottom:22px;align-items:flex-start}
.copyright{position:absolute;left:0;top:4180px;width:1200px;height:60px;border-top:1px solid #ddd;text-align:center;padding-top:24px;font-size:11.5px;color:#333}
.copyright b{color:var(--red);font-weight:500}
</style>
</head>
<body>

<header class="site-header">
  <div class="brand"><span class="brand-dot"></span>Brightline Tint</div>
  <nav class="nav">
    <span class="active">Home</span><span>Auto</span><span>Commercial</span><span>Paint Protection</span><span>Detailing</span><span>Portfolio</span>
  </nav>
  <div class="header-phone">+1 (555) 014-2290</div>
  <div class="btn header-cta">Contact Us</div>
</header>

<section class="hero" role="img" aria-label="Technician applying window tint film to a grey car door in a workshop">
  <svg class="hero-accent" viewBox="0 0 1200 612" aria-hidden="true">
    <polygon points="0,0 400,0 140,612 0,612" fill="#1f2125" opacity=".55"/>
    <polygon points="260,0 440,0 300,260 210,120" fill="#8d1620" opacity=".55"/>
  </svg>
  <h1 class="hero-title display">Your Window<br>Tinting</h1>
  <div class="hero-tags"><span>Commercial</span><span>Residential</span></div>
  <div class="btn hero-cta">Get Started</div>
  <div class="hero-rule"></div>
  <div class="hero-links" style="left:140px">Shipping Logistics</div>
  <div class="hero-links" style="left:447px">Intermodal Shipping</div>
  <div class="hero-links" style="left:736px">Brokerage</div>
  <div class="hero-links" style="left:975px">Dispatch Services</div>
</section>

<section class="services">
  <h2 class="section-title">Our Services</h2>
  <p class="lead">It is a long established fact that a reader will be distracted by the readable content<br>of a page when looking at its layout.</p>

  <article class="service-card" style="left:170px">
    <svg width="66" height="72" viewBox="0 0 66 72" fill="none" stroke="#d42030" stroke-width="1.6"><polygon points="33,2 63,19 63,53 33,70 3,53 3,19"/><rect x="20" y="24" width="26" height="22" rx="3"/><line x1="20" y1="34" x2="46" y2="34"/></svg>
    <h3>Window Tinting</h3>
    <p>There are many variations of passages of Lorem Ipsum available, but the majority have suffered alteration.</p>
    <span class="more">Learn More</span>
  </article>
  <article class="service-card" style="left:469px">
    <svg width="66" height="72" viewBox="0 0 66 72" fill="none" stroke="#d42030" stroke-width="1.6"><polygon points="33,2 63,19 63,53 33,70 3,53 3,19"/><rect x="20" y="22" width="24" height="28" rx="2"/><line x1="26" y1="44" x2="42" y2="28"/></svg>
    <h3>Paint Protection</h3>
    <p>There are many variations of passages of Lorem Ipsum available, but the majority have suffered alteration.</p>
    <span class="more">Learn More</span>
  </article>
  <article class="service-card" style="left:768px">
    <svg width="66" height="72" viewBox="0 0 66 72" fill="none" stroke="#d42030" stroke-width="1.6"><polygon points="33,2 63,19 63,53 33,70 3,53 3,19"/><rect x="17" y="28" width="32" height="14" rx="3"/><circle cx="24" cy="44" r="3"/><circle cx="42" cy="44" r="3"/></svg>
    <h3>Automotive Detailing</h3>
    <p>There are many variations of passages of Lorem Ipsum available, but the majority have suffered alteration.</p>
    <span class="more">Learn More</span>
  </article>
  <div class="btn all-services">See All Services</div>
</section>

<section class="why">
  <h2 class="section-title">Why Us</h2>
  <p class="lead">If you use this site regularly and would like to help keep the site on the Internet,<br>please consider donating a small sum to help pay.</p>
  <div class="btn why-cta">See Our Work</div>

  <div class="stat" style="left:167px;top:168px;width:260px;height:230px">
    <svg width="260" height="230" viewBox="0 0 260 230" fill="none">
      <path d="M20,130 A110,110 0 1 1 240,118" stroke="#5f86a4" stroke-width="8"/>
      <circle cx="20" cy="130" r="9" fill="#fff" stroke="#5f86a4" stroke-width="5"/>
      <circle cx="130" cy="120" r="86" fill="#fff" stroke="#5f86a4" stroke-width="5"/>
    </svg>
    <div class="stat-num" style="top:80px;font-size:72px;color:var(--steel)">05</div>
    <div class="stat-label" style="top:155px;color:var(--steel)">Years of<br>Experience</div>
  </div>

  <div class="stat" style="left:470px;top:276px;width:272px;height:250px">
    <svg width="272" height="250" viewBox="0 0 272 250" fill="none">
      <path d="M20,100 A116,116 0 1 0 252,100" stroke="#d42030" stroke-width="8"/>
      <circle cx="20" cy="100" r="9" fill="#fff" stroke="#d42030" stroke-width="5"/>
      <circle cx="136" cy="110" r="88" fill="#fff" stroke="#d42030" stroke-width="5"/>
    </svg>
    <div class="stat-num" style="top:48px;font-size:76px;color:var(--red)">100</div>
    <div class="stat-label" style="top:128px;color:var(--red)">Successful<br>Installations</div>
  </div>

  <div class="stat" style="left:783px;top:176px;width:260px;height:230px">
    <svg width="260" height="230" viewBox="0 0 260 230" fill="none">
      <path d="M20,130 A110,110 0 1 1 240,118" stroke="#5f86a4" stroke-width="8"/>
      <circle cx="20" cy="130" r="9" fill="#fff" stroke="#5f86a4" stroke-width="5"/>
      <circle cx="130" cy="120" r="86" fill="#fff" stroke="#5f86a4" stroke-width="5"/>
    </svg>
    <div class="stat-num" style="top:80px;font-size:72px;color:var(--steel)">30</div>
    <div class="stat-label" style="top:160px;color:var(--steel)">5 Star Reviews</div>
  </div>
</section>

<section class="work">
  <h2 class="section-title">Our Work</h2>
  <div class="work-tile" style="left:168px;top:157px;background:linear-gradient(160deg,#9aa0a6,#3b3e42 70%,#1d1f22)" role="img" aria-label="Technician applying a vinyl wrap to a vehicle"><span>Vehicle Wraps</span></div>
  <div class="work-tile" style="left:620px;top:157px;background:linear-gradient(150deg,#3a3d42,#111214 60%,#2a2b2d)" role="img" aria-label="Squeegee smoothing protection film on dark paint"><span>Paint Protection</span></div>
  <div class="work-tile" style="left:168px;top:532px;background:linear-gradient(160deg,#8d9196,#c98a1c 50%,#3d2a10)" role="img" aria-label="Orange sports car parked outside a workshop"><span>Caliper Wraps</span></div>
  <div class="work-tile" style="left:620px;top:532px;background:linear-gradient(160deg,#e6e8ea,#b7bcc1 55%,#2c2f33)" role="img" aria-label="Front of a white car with blacked out trim"><span>Chrome Deletes</span></div>
</section>

<section class="testimonials">
  <h2 class="section-title">Our Testimonials</h2>

  <article class="quote-card" style="left:132px;top:3060px;width:293px;height:283px">
    <div class="avatar" role="img" aria-label="Customer portrait" style="top:-36px;width:70px;height:70px;background:#6d6a66"></div>
    <div class="quote-mark" style="margin-top:56px">&ldquo;</div>
    <p style="margin:6px 22px 0">Lorem Ipsum is simply dummy text of the printing and typesetting industry. Lorem Ipsum has been the industry's standard dummy text ever since the 1500s.</p>
    <h4>Marco D.</h4>
    <div class="stars">★★★★★</div>
  </article>

  <article class="quote-card" style="left:810px;top:3060px;width:285px;height:283px">
    <div class="avatar" role="img" aria-label="Customer portrait" style="top:-36px;width:70px;height:70px;background:#5a5650"></div>
    <div class="quote-mark" style="margin-top:56px">&ldquo;</div>
    <p style="margin:6px 22px 0">Lorem Ipsum is simply dummy text of the printing and typesetting industry. Lorem Ipsum has been the industry's standard dummy text ever since the 1500s.</p>
    <h4>Dana W.</h4>
    <div class="stars">★★★★★</div>
  </article>

  <article class="quote-card" style="left:427px;top:3032px;width:381px;height:350px">
    <div class="avatar" role="img" aria-label="Customer portrait" style="top:-42px;width:84px;height:84px;background:#8a3b3b"></div>
    <div class="quote-mark" style="margin-top:66px">&ldquo;</div>
    <p style="margin:6px 28px 0">Lorem Ipsum is simply dummy text of the printing and typesetting industry. Lorem Ipsum has been the industry's standard dummy text ever since the 1500s, when an unknown printer took a galley of type and scrambled it to make a type specimen book. It has</p>
    <h4>Elena P.</h4>
    <div class="stars">★★★★★</div>
  </article>
</section>

<div class="foot-band"></div>

<section class="project">
  <div class="abs" role="img" aria-label="Mechanic in blue overalls working on a red car" style="left:508px;top:0;width:468px;height:380px;background:linear-gradient(110deg,rgba(195,204,212,0) 0%,#2f58b8 30%,#1e3f8c 60%,#b8202a 100%)"></div>
  <h2 class="display">Tell Us About Your Project</h2>
  <p>It is a long established fact that a reader will be distracted by the readable content of a page when looking at its layout. The point of using Lorem Ipsum is that it has a more-or-less normal.</p>
  <div class="signup"><span>Your Email Address</span><span class="btn">Get A Free Estimate</span></div>
</section>

<footer>
  <div class="footer-brand"><span class="brand-dot"></span>Brightline Tint</div>
  <p class="footer-about">Lorem Ipsum is simply dummy text of the printing and typesetting industry. Lorem Ipsum has been the industry's standard dummy text.</p>
  <div class="socials" aria-label="Social links"><span></span><span></span><span></span><span></span></div>

  <div class="foot-col" style="left:486px">
    <h5>Quick Links</h5>
    <ul><li>Home</li><li>Auto</li><li>Commercial</li><li>Paint Protection</li><li>Detailing</li><li>Portfolio</li></ul>
  </div>
  <div class="foot-col" style="left:676px">
    <h5>Works</h5>
    <ul><li>Vehicle Wraps</li><li>Paint Protection</li><li>Caliper Wraps</li><li>Chrome Deletes</li></ul>
  </div>
  <div class="foot-col" style="left:876px">
    <h5>Contact Us</h5>
    <div style="margin-top:16px">
      <div class="contact-row"><svg width="16" height="12" viewBox="0 0 16 12"><rect width="16" height="12" rx="1" fill="#d42030"/><path d="M1,1 L8,7 L15,1" stroke="#fff" stroke-width="1.4" fill="none"/></svg>info@brightlinetint.com</div>
      <div class="contact-row"><svg width="16" height="16" viewBox="0 0 24 24"><path d="M6.6 10.8a15 15 0 0 0 6.6 6.6l2.2-2.2c.3-.3.7-.4 1-.2 1.1.4 2.3.6 3.6.6.6 0 1 .4 1 1V20c0 .6-.4 1-1 1A17 17 0 0 1 3 4c0-.6.4-1 1-1h3.5c.6 0 1 .4 1 1 0 1.2.2 2.4.6 3.6.1.3 0 .7-.2 1z" fill="#d42030"/></svg>(555) 014-2290</div>
      <div class="contact-row"><svg width="14" height="18" viewBox="0 0 14 18"><path d="M7 0a7 7 0 0 0-7 7c0 5 7 11 7 11s7-6 7-11a7 7 0 0 0-7-7z" fill="#d42030"/><circle cx="7" cy="7" r="2.6" fill="#fff"/></svg>2140 Harbor Lane,<br>Stockton, CA</div>
    </div>
  </div>

  <div class="copyright">Copyright © 2023 <b>Window Tinting</b>, All Received</div>
</footer>

</body>
</html>
```